Larder & Hearth - Premium Catering needs a new menu design.

I currently use menupro to make my own menus for printing and uploading to the website (PDF). I need a professional menu to replace my current menu. I wold like to mail these menus out so I'm thinking a tri-fold menu would be the best option. Similar to what pizzerias send out.

Need extra days to review

Logo Text

Would be good to reduce the text thickness of the letters "TIL" in the word TILMORE. Right now TIL has thicker text.

Colors

Designer to choose colors to be used in the design.

```html
<!DOCTYPE html>
<html lang="en">
<head>
<meta charset="utf-8">
<title>Tilmore Deli Menu</title>
<link href="https://fonts.googleapis.com/css2?family=Source+Sans+3:wght@400;500;600;700&display=swap" rel="stylesheet">
<style>
:root{
  --backdrop:#555555;
  --paper:#ffffff;
  --gold:#b8952f;
  --wine:#8b1a1a;
  --ink:#232323;
  --leaf:#4d8a2a;
}
*{margin:0;padding:0;box-sizing:border-box}
html,body{width:1200px;height:1200px;overflow:hidden;background:var(--backdrop)}
body{font-family:"Source Sans 3",sans-serif;position:relative}
.page{position:absolute;left:155px;top:25px;width:890px;height:1150px;background:var(--paper)}
.frame{position:absolute;left:170px;top:39px;width:861px;height:1121px;border:2px solid var(--gold)}
.column{position:absolute;top:0;width:370px;height:1200px}
.column--left{left:206px}
.column--right{left:627px}
.divider{position:absolute;left:599px;top:127px;width:1.5px;height:1000px;
  background:repeating-linear-gradient(to bottom,var(--gold) 0 7px,transparent 7px 13px)}
.dash-rule{position:absolute;left:0;width:367px;height:1.5px;
  background:repeating-linear-gradient(to right,var(--gold) 0 7px,transparent 7px 12px)}
.heading{position:absolute;display:flex;align-items:center;color:var(--gold);font-weight:700;text-transform:uppercase;white-space:nowrap}
.heading .bar{width:25px;height:4px;background:var(--gold);flex:none}
.heading--small{left:0;width:367px;top:73px;height:24px;justify-content:space-between;font-size:22px;letter-spacing:1.6px}
.heading--large{font-size:34px;letter-spacing:2px;height:40px}
.subtitle{position:absolute;left:0;width:367px;text-align:center;color:var(--gold);font-weight:600;font-size:11px;line-height:14.6px;text-transform:uppercase}
.item{position:absolute;left:0;width:370px}
.item .row{display:flex;align-items:center;height:24px}
.name{color:var(--wine);font-weight:600;font-size:19.5px;letter-spacing:-0.1px;white-space:nowrap}
.rule{flex:1;height:1px;background:var(--gold);margin:0 6px 0 12px}
.price{color:var(--wine);font-weight:700;font-size:13.5px;white-space:nowrap;width:38px;text-align:left}
.price--wide{width:46px}
.desc{color:var(--ink);font-weight:500;font-size:11px;line-height:14px;white-space:nowrap}
.tag{display:inline-flex;flex-direction:column;align-items:center;margin-left:5px;vertical-align:middle;line-height:1}
.tag small{font-size:6px;font-weight:500}
.tag--spicy small{color:var(--wine)}
.tag--veggie small{color:var(--wine)}
.extra{position:absolute;left:0;display:flex;align-items:center;height:16px}
.extra .name{font-size:14px;font-weight:500;width:78px}
.extra .rule{flex:none;width:42px;margin:0 6px 0 0}
.extra .price{font-size:12px}
.fine{position:absolute;left:0;width:370px;color:var(--gold);font-weight:600;font-size:7.4px;text-transform:uppercase;white-space:nowrap}
.choice{position:absolute;left:0;color:var(--gold);font-size:10.8px;font-weight:400;text-transform:uppercase;white-space:nowrap}
.choice b{font-weight:600}
.order{position:absolute;left:494px;top:1134px;width:212px;text-align:center;color:var(--gold);font-weight:600;font-size:11.5px;letter-spacing:.2px}
.order-bracket{position:absolute;left:494px;top:1147px}
</style>
</head>
<body>
<div class="page"></div>
<div class="frame"></div>
<div class="divider"></div>

<section class="column column--left">
  <h2 class="heading heading--small"><span class="bar"></span>Pressure Fried Chicken<span class="bar"></span></h2>
  <div class="dash-rule" style="top:128px"></div>
  <p class="subtitle" style="top:154px">Served with mashed and gravy or seasoned<br>potato wedges, coleslaw and dinner rolls</p>
  <div class="dash-rule" style="top:212px"></div>

  <div class="item" style="top:218px"><div class="row"><span class="name">2-Piece</span><span class="rule"></span><span class="price">$ 6.99</span></div><p class="desc">Leg and thigh.</p></div>
  <div class="dash-rule" style="top:260px"></div>
  <div class="item" style="top:266px"><div class="row"><span class="name">3-Piece</span><span class="rule"></span><span class="price">$ 7.99</span></div><p class="desc">Leg, thigh, and wing.</p></div>
  <div class="dash-rule" style="top:307px"></div>
  <div class="item" style="top:313px"><div class="row"><span class="name">4-Piece</span><span class="rule"></span><span class="price">$ 9.99</span></div><p class="desc">Breast, leg, thigh, and wing.</p></div>
  <div class="dash-rule" style="top:355px"></div>
  <div class="item" style="top:361px"><div class="row"><span class="name">Family Meal</span><span class="rule"></span><span class="price price--wide">$ 19.49</span></div><p class="desc">Two thighs, two legs, two breasts, and two wings.</p></div>
  <div class="dash-rule" style="top:402px"></div>

  <h2 class="heading heading--large" style="left:0;width:370px;top:422px;justify-content:space-between"><span class="bar"></span>Hot Sandwiches<span class="bar"></span></h2>
  <p class="subtitle" style="top:462px">Served with complementary french fries</p>
  <div class="dash-rule" style="top:493px"></div>

  <div class="item" style="top:494px"><div class="row"><span class="name">Brooklyn Reuben</span><span class="rule"></span><span class="price">$ 8.99</span></div><p class="desc" style="margin-top:3px">Corned beef, coleslaw, Russian dressing, and Swiss cheese on grilled rye.</p></div>
  <div class="dash-rule" style="top:537px"></div>
  <div class="item" style="top:541px"><div class="row"><span class="name">Buffalo Chicken Cutlet Deluxe</span><span class="rule"></span><span class="price">$ 8.99</span></div><p class="desc" style="margin-top:4px">Topped with lettuce, tomato, onion, and bleu cheese dressing<br>on a kaiser roll.</p></div>
  <div class="dash-rule" style="top:596px"></div>
  <div class="item" style="top:601px"><div class="row"><span class="name">Cajun Chicken Quesadilla</span><span class="tag tag--spicy"><svg width="16" height="9" viewBox="0 0 16 9"><path d="M1 6 C5 8 11 6 13 2 L15 1 L14 3 C12 7 6 9 1 6Z" fill="#c8201e"/><path d="M13 2 L15 0" stroke="#3a7a1e" stroke-width="1.2"/></svg><small>spicy</small></span><span class="rule"></span><span class="price">$ 9.99</span></div><p class="desc" style="margin-top:4px">Grilled Cajun chicken breast, chopped bacon, and melted cheddar cheese<br>on a toasted tortilla served with sour cream and salsa.</p></div>
  <div class="dash-rule" style="top:657px"></div>
  <div class="item" style="top:662px"><div class="row"><span class="name">Chicken Breast Parmigiana</span><span class="rule"></span><span class="price">$ 8.99</span></div><p class="desc">On a torpedo roll.</p></div>
  <div class="dash-rule" style="top:701px"></div>
  <div class="item" style="top:704px"><div class="row"><span class="name">French Dip</span><span class="rule"></span><span class="price">$ 9.99</span></div><p class="desc" style="margin-top:3px">Homemade roast beef on a toasted garlic roll served with Au Jus.</p></div>
  <div class="dash-rule" style="top:749px"></div>
  <div class="item" style="top:756px"><div class="row"><span class="name">Grilled Cheese</span><span class="tag tag--veggie"><svg width="16" height="8" viewBox="0 0 16 8"><path d="M8 8 C4 7 1 4 1 1 C5 1 8 4 8 8Z M8 8 C12 7 15 4 15 1 C11 1 8 4 8 8Z" fill="#4d8a2a"/></svg><small>(veggie)</small></span><span class="rule"></span><span class="price">$ 6.99</span></div></div>
  <div class="dash-rule" style="top:783px"></div>
  <div class="item" style="top:792px"><div class="row"><span class="name">Hot Pastrami</span><span class="rule"></span><span class="price">$ 8.99</span></div><p class="desc">Grilled pastrami on grilled rye bread with deli mustard.</p></div>
  <div class="dash-rule" style="top:835px"></div>
  <div class="item" style="top:839px"><div class="row"><span class="name">NY Reuben</span><span class="rule"></span><span class="price">$ 8.99</span></div><p class="desc">Corned beef, sauerkraut, Russian dressing, and Swiss cheese on grilled rye.</p></div>
  <div class="dash-rule" style="top:882px"></div>
  <div class="item" style="top:887px"><div class="row"><span class="name">Meatball Parmigiana</span><span class="rule"></span><span class="price">$ 9.49</span></div><p class="desc">Topped with provolone cheese and homemade sauce on a torpedo roll.</p></div>
  <div class="dash-rule" style="top:930px"></div>
  <div class="item" style="top:935px"><div class="row"><span class="name">Turkey Reuben</span><span class="rule"></span><span class="price">$ 8.99</span></div><p class="desc">Oven roasted turkey, coleslaw, Russian dressing, and Swiss cheese<br>on grilled rye.</p></div>
  <div class="dash-rule" style="top:990px"></div>
  <div class="item" style="top:994px"><div class="row"><span class="name">Cowboy Chicken</span><span class="rule"></span><span class="price">$ 9.99</span></div><p class="desc">Grilled chicken breast topped with sautéed fresh mushrooms, bacon,<br>Monterey Jack cheese, and honey mustard on grilled sourdough bread.</p></div>
  <div class="dash-rule" style="top:1048px"></div>
  <div class="item" style="top:1054px"><div class="row"><span class="name">Cajun Chicken Express</span><span class="tag tag--spicy"><svg width="16" height="9" viewBox="0 0 16 9"><path d="M1 6 C5 8 11 6 13 2 L15 1 L14 3 C12 7 6 9 1 6Z" fill="#c8201e"/><path d="M13 2 L15 0" stroke="#3a7a1e" stroke-width="1.2"/></svg><small>spicy</small></span><span class="rule"></span><span class="price">$ 9.99</span></div><p class="desc" style="margin-top:4px">Sautéed Cajun chicken breast dipped in Louisiana hot sauce and topped<br>with sautéed mushrooms, blue cheese dressing, and melted Monterey Jack<br>cheese on grilled sourdough bread.</p></div>
  <div class="dash-rule" style="top:1126px"></div>
</section>

<section class="column column--right">
  <h2 class="heading heading--large" style="left:81px;top:58px;gap:12px;font-size:36px;letter-spacing:3px"><span class="bar"></span>Salads<span class="bar"></span></h2>
  <div class="dash-rule" style="top:128px"></div>
  <p class="subtitle" style="top:134px">Served with your choise of dressing: French, Russian,<br>bleu cheese, ranch, creamy Italian, oil &amp; vinegar, ceaser,<br>honey mustard, house (oil &amp; vinegar &amp; house seasoning)<br>homemade balsamic vinaigrette. Fat free ressing: Italian,<br>honey dijon or ranch</p>
  <div class="dash-rule" style="top:210px"></div>

  <div class="item" style="top:214px"><div class="row"><span class="name">Tossed Salad</span><span class="rule" style="margin-left:18px"></span><span class="price">$ 7.49</span></div><p class="desc">Mixed greens topped with tomato wedges, cucumbers, green peppers,<br>Greek olives, and red onions served with choice of dressing.</p></div>
  <div class="dash-rule" style="top:272px"></div>
  <div class="item" style="top:277px"><div class="row"><span class="name">Athenian Chicken Salad</span><span class="rule"></span><span class="price">$ 8.99</span></div><p class="desc">Grilled marinated chicken breast over a diced Greek salad served with olive<br>oil &amp; vinegar dressing.</p></div>
  <div class="dash-rule" style="top:335px"></div>
  <div class="item" style="top:340px"><div class="row"><span class="name">Buffalo Crispy Chicken Salad</span><span class="rule"></span><span class="price">$ 9.49</span></div><p class="desc">Mixed greens topped with tomato wedges, Greek olives, strips of deep<br>fried buffalo chicken cutlet, and crispy tortilla chip slices served with<br>choice of dressing.</p></div>
  <div class="dash-rule" style="top:411px"></div>
  <div class="item" style="top:416px"><div class="row"><span class="name">Chicken Caesar</span><span class="rule"></span><span class="price">$ 8.99</span></div><p class="desc">Mixed greens topped with fresh grilled chicken breast, tomato wedges,<br>Greek olives, sprinkled Romano cheese, croutons, and red onions served<br>with Caesar dressing.</p></div>
  <div class="dash-rule" style="top:487px"></div>
  <div class="item" style="top:492px"><div class="row"><span class="name">Cajun Chicken Caesar</span><span class="rule"></span><span class="price">$ 8.99</span></div><p class="desc">Mixed greens topped with fresh grilled Cajun chicken breast,<br>tomato wedges, Greek olives, sprinkled Romano cheese, croutons,<br>and red onions served with Caesar dressing.</p></div>
  <div class="dash-rule" style="top:563px"></div>
  <div class="item" style="top:567px"><div class="row"><span class="name">Chef</span><span class="rule"></span><span class="price">$ 8.99</span></div><p class="desc" style="margin-top:3px">Tossed salad topped with hard boiled egg and sliced roast beef, ham,<br>turkey, and Swiss cheese served with choice of dressing.</p></div>
  <div class="dash-rule" style="top:627px"></div>
  <div class="item" style="top:631px"><div class="row"><span class="name">Cobb with Chicken Breast</span><span class="rule"></span><span class="price">$ 9.99</span></div><p class="desc" style="margin-top:3px">Mixed romaine and iceberg lettuce topped with grilled chicken<br>breast, chopped bacon, tomatoes, hard boiled egg, Greek olives,<br>fresh mushrooms,&nbsp; red onions, and sprinkled with bleu cheese and<br>Romano served with choice of dressing.</p></div>
  <div class="dash-rule" style="top:717px"></div>
  <div class="item" style="top:722px"><div class="row"><span class="name">Southwestern</span><span class="tag tag--spicy"><svg width="16" height="9" viewBox="0 0 16 9"><path d="M1 6 C5 8 11 6 13 2 L15 1 L14 3 C12 7 6 9 1 6Z" fill="#c8201e"/><path d="M13 2 L15 0" stroke="#3a7a1e" stroke-width="1.2"/></svg><small>spicy</small></span><span class="rule"></span><span class="price">$ 9.99</span></div><p class="desc" style="margin-top:3px">Mixed greens topped with Cajun chicken breast, shredded cheddar<br>cheese, scallions, tomatoes, Greek olives, red onions, hard boiled egg,<br>and crispy tortilla chip slices sprinkled with Romano cheese served with<br>choice of dressing.</p></div>
  <div class="dash-rule" style="top:808px"></div>

  <span class="heading" style="left:20px;top:854px"><span class="bar"></span></span>
  <span class="heading" style="left:323px;top:854px"><span class="bar"></span></span>
  <h2 class="heading heading--large" style="left:0;width:373px;top:824px;height:auto;flex-direction:column;line-height:32px;text-align:center">Lunch &amp;<br>Dinner Pasta</h2>
  <div class="dash-rule" style="top:914px"></div>
  <div class="item" style="top:919px"><div class="row"><span class="name" style="width:144px">Lunch</span><span class="rule" style="margin-left:0"></span><span class="price">$ 7.25</span></div><p class="desc" style="margin-top:3px">Served with garlic crostini</p></div>
  <div class="dash-rule" style="top:965px"></div>
  <div class="item" style="top:970px"><div class="row"><span class="name" style="width:144px">Dinner</span><span class="rule" style="margin-left:0"></span><span class="price">$ 9.95</span></div><p class="desc" style="margin-top:3px">Served with garlic bread and soup or tossed salad</p></div>
  <div class="dash-rule" style="top:1016px"></div>
  <div class="extra" style="top:1023px"><span class="name">Extra lunch</span><span class="rule"></span><span class="price">$ 1.95</span></div>
  <div class="extra" style="top:1039px"><span class="name">Extra dinner</span><span class="rule"></span><span class="price">$ 2.95</span></div>
  <p class="fine" style="top:1062px">Homemade meatballs, Italian sausage, sautéed chicken, meat sauce, cheese ravioli</p>
  <p class="choice" style="top:1088px"><b>Choose your pasta:</b> penne, rigatoni, linguini</p>
  <p class="choice" style="top:1103px"><b>Choose your sauce:</b> marinara, olive oil &amp; garlic, vodka-pink sauce</p>
  <div class="dash-rule" style="top:1126px"></div>
</section>

<p class="order">ORDER ONLINE @TILMOREDELI.COM</p>
<svg class="order-bracket" width="212" height="6" viewBox="0 0 212 6"><path d="M1 0 V5 H211 V0" fill="none" stroke="#b8952f" stroke-width="1.5"/></svg>
</body>
</html>
```